Family Entertainment Center needs a fundraising flyer design

We need a 8.5 x 5.5 (half sheet of copy paper) flyer designed for a roller skating rink/family entertainment center in Wichita, KS. We partner with 100s of local schools each year by offering PTO fundraisers at our facility. With each party we send out flyers to the schools to send home with each kid to remind them of the time and date of the party as well as get them excited! Most of these schools and PTOs call these fundraisers "skate night".The information we need communicated or on our flyer is below:-Skating $6-Play Zone $6-Skate & Play $10-Skate Rental is included in above pricing-Price is per person-www.pinwheelrollks.com-Pinwheel Roll Center 587 S. Elmridge Ave. Wichita, KS 67219-Our logo (attached)-The words or heading "Skate Night"-A blank, white space for us to print details in (see attached flyer for an example)

Target Market(s)

Elementary School parents and kids

Requirements
Must have
• The information outlined in the description and a blank white space incorporated into the design for our ability to print over.
Nice to have
• colors that match or compliment our logo, creative, but clean fonts

```html
<!DOCTYPE html>
<html lang="en">
<head>
<meta charset="utf-8">
<title>Skate Night – Pinwheel Roll Center</title>
<link rel="stylesheet" href="https://fonts.googleapis.com/css2?family=Montserrat:wght@500;600;700&family=Permanent+Marker&family=Source+Sans+3:ital,wght@0,400;0,600;1,400&display=swap">
<style>
  :root {
    --navy: #3d4c9c;
    --navy-deep: #323f86;
    --pink: #e9487b;
    --pink-deep: #d23c6b;
    --blush: #f6c8d7;
    --peach: #f8dcb6;
    --white: #ffffff;
    --ink: #222222;
  }
  html, body {
    margin: 0;
    padding: 0;
    overflow: hidden;
    background: var(--white);
  }
  .flyer {
    position: relative;
    width: 777px;
    height: 1200px;
    overflow: hidden;
    background: var(--white);
    font-family: "Source Sans 3", Arial, sans-serif;
  }
  .artwork {
    position: absolute;
    inset: 0;
    width: 777px;
    height: 1200px;
  }
  .brand {
    position: absolute;
    top: 62px;
    right: 40px;
    width: 250px;
    text-align: right;
  }
  .brand-line {
    display: flex;
    align-items: center;
    justify-content: flex-end;
    gap: 10px;
  }
  .brand-dot {
    flex: none;
    width: 18px;
    height: 18px;
    border-radius: 50%;
    background: var(--pink);
  }
  .brand-name {
    font-family: "Montserrat", Arial, sans-serif;
    font-weight: 700;
    font-size: 22px;
    line-height: 1.1;
    color: var(--navy);
  }
  .address {
    margin: 8px 0 0;
    font-size: 15px;
    line-height: 1.35;
    color: var(--navy);
  }
  .website {
    position: absolute;
    top: 207px;
    left: 502px;
    display: flex;
    align-items: center;
    gap: 12px;
    font-size: 18px;
    color: var(--navy);
  }
  .website svg { width: 16px; height: 12px; }
  .headline-skate {
    position: absolute;
    top: 462px;
    left: 345px;
    margin: 0;
    font-family: "Permanent Marker", "Arial Black", Impact, sans-serif;
    font-weight: 400;
    font-size: 118px;
    line-height: 1;
    color: var(--pink);
    transform: skewX(-8deg);
    letter-spacing: -1px;
    white-space: nowrap;
  }
  .headline-night {
    position: absolute;
    top: 596px;
    right: 66px;
    margin: 0;
    font-family: "Montserrat", Arial, sans-serif;
    font-weight: 600;
    font-size: 92px;
    line-height: 1;
    letter-spacing: 3px;
    color: var(--navy);
  }
  .print-space {
    position: absolute;
    top: 720px;
    left: 380px;
    width: 340px;
    height: 330px;
  }
  .pricing {
    position: absolute;
    top: 862px;
    left: 48px;
    width: 262px;
    border-radius: 14px;
    overflow: hidden;
  }
  .price-row {
    display: flex;
    height: 59px;
    color: var(--white);
  }
  .price-label {
    flex: 1;
    display: flex;
    align-items: center;
    padding-left: 18px;
    font-size: 23px;
    background: var(--navy);
  }
  .price-value {
    width: 75px;
    display: flex;
    align-items: center;
    justify-content: center;
    font-size: 22px;
    background: var(--pink);
  }
  .price-value strong { font-weight: 600; }
  .price-row--alt .price-label { background: var(--navy-deep); }
  .price-row--alt .price-value { background: var(--pink-deep); }
  .pricing-note {
    position: absolute;
    top: 1056px;
    left: 48px;
    margin: 0;
    font-style: italic;
    font-size: 14px;
    line-height: 1.45;
    color: var(--ink);
  }
</style>
</head>
<body>
<main class="flyer">
  <svg class="artwork" viewBox="0 0 600 927" xmlns="http://www.w3.org/2000/svg">
    <defs>
      <linearGradient id="grad-group" x1="0" y1="0" x2="1" y2="1">
        <stop offset="0" stop-color="#8a6f68"/>
        <stop offset="0.5" stop-color="#c7a98a"/>
        <stop offset="1" stop-color="#5b4a5e"/>
      </linearGradient>
      <linearGradient id="grad-rink" x1="0" y1="0" x2="1" y2="1">
        <stop offset="0" stop-color="#7d8fb8"/>
        <stop offset="0.5" stop-color="#d9dce8"/>
        <stop offset="1" stop-color="#eef0f5"/>
      </linearGradient>
      <linearGradient id="grad-boy" x1="0" y1="0" x2="1" y2="1">
        <stop offset="0" stop-color="#3a5a3a"/>
        <stop offset="0.5" stop-color="#d8b497"/>
        <stop offset="1" stop-color="#4b6a9c"/>
      </linearGradient>
      <linearGradient id="grad-play" x1="0" y1="0" x2="1" y2="1">
        <stop offset="0" stop-color="#5c5f7a"/>
        <stop offset="0.5" stop-color="#c4a5a8"/>
        <stop offset="1" stop-color="#6e8a7c"/>
      </linearGradient>
    </defs>

    <g class="decor" stroke-linecap="round" fill="none">
      <line x1="200" y1="4" x2="262" y2="50" stroke="var(--blush)" stroke-width="10"/>
      <line x1="255" y1="12" x2="370" y2="95" stroke="var(--peach)" stroke-width="3"/>
      <line x1="230" y1="120" x2="280" y2="160" stroke="var(--peach)" stroke-width="4"/>
      <line x1="60" y1="260" x2="110" y2="218" stroke="var(--pink)" stroke-width="10"/>
      <line x1="460" y1="215" x2="560" y2="305" stroke="var(--blush)" stroke-width="16"/>
      <line x1="552" y1="270" x2="598" y2="318" stroke="var(--pink)" stroke-width="5"/>
      <line x1="395" y1="205" x2="420" y2="225" stroke="var(--blush)" stroke-width="4"/>
      <line x1="0" y1="560" x2="40" y2="528" stroke="var(--peach)" stroke-width="5"/>
      <line x1="0" y1="632" x2="60" y2="590" stroke="var(--blush)" stroke-width="4"/>
    </g>
    <circle cx="567" cy="317" r="9" fill="var(--blush)"/>
    <circle cx="262" cy="133" r="3" fill="var(--pink)"/>
    <g class="dot-trail" fill="var(--pink)">
      <circle cx="4" cy="582" r="1.6"/><circle cx="14" cy="573" r="1.6"/><circle cx="24" cy="564" r="1.6"/>
      <circle cx="34" cy="555" r="1.6"/><circle cx="44" cy="546" r="1.6"/><circle cx="54" cy="537" r="1.6"/>
      <circle cx="64" cy="528" r="1.6"/><circle cx="74" cy="519" r="1.6"/>
      <circle cx="10" cy="600" r="1.6"/><circle cx="20" cy="591" r="1.6"/>
    </g>
    <circle cx="205" cy="868" r="6" fill="var(--blush)"/>
    <circle cx="228" cy="883" r="10" fill="var(--blush)"/>
    <circle cx="224" cy="858" r="3" fill="var(--blush)"/>

    <polygon points="0,0 218,0 276,100 136,242 0,242" fill="url(#grad-group)" role="img" aria-label="Photo: group of cheering schoolkids at the skate center"/>
    <polygon points="290,122 460,295 300,468 116,292" fill="url(#grad-rink)" role="img" aria-label="Photo: young girl roller skating on the rink"/>
    <polygon points="0,262 118,262 160,380 34,518 0,518" fill="url(#grad-boy)" role="img" aria-label="Photo: smiling boy at the skate night"/>
    <polygon points="190,380 300,482 182,586 70,482" fill="url(#grad-play)" role="img" aria-label="Photo: two girls giving a high five in the play zone"/>
  </svg>

  <div class="brand">
    <div class="brand-line">
      <span class="brand-dot"></span>
      <span class="brand-name">Pinwheel Roll Center</span>
    </div>
    <p class="address">587 S. Elmridge Ave.<br>Wichita, KS 67219</p>
  </div>

  <div class="website">
    <svg viewBox="0 0 16 12" aria-hidden="true">
      <rect x="0" y="0" width="16" height="12" rx="1" fill="var(--navy)"/>
      <polyline points="1,1 8,7 15,1" fill="none" stroke="#fff" stroke-width="1.4"/>
    </svg>
    <span>www.pinwheelrollks.com</span>
  </div>

  <h1 class="headline-skate">SKATE</h1>
  <h2 class="headline-night">NIGHT</h2>

  <div class="print-space" aria-label="Blank space for event details"></div>

  <div class="pricing">
    <div class="price-row"><span class="price-label">Skating</span><span class="price-value">$<strong>6</strong></span></div>
    <div class="price-row price-row--alt"><span class="price-label">Play Zone</span><span class="price-value">$<strong>6</strong></span></div>
    <div class="price-row"><span class="price-label">Skate &amp; Play</span><span class="price-value">$<strong>10</strong></span></div>
  </div>
  <p class="pricing-note">Skate Rental is included in above pricing.<br>Price is per person.</p>
</main>
</body>
</html>
```